Business Card Design - Service Company

Use of the card mainly in living rooms and relations b2b We wish a card with a modern design, blue tones in the background would be a plus The card must be front / back (one side with the logo / the other with the information of contact )

Font styles to use
Serif

Requirements
Must have
• Using the map on the back of the business card Editable format! Photoshop CS2 / Illustrator CS2
Nice to have
• Maquis Vertex IT Pierre Blanche Commercial Center, 20480 Lorvanu 0495718243 Siret 71384096200018 APE 6203Y https://www.fb.com/ateliertech.maquisvertex www.maquis-vertex.com

```html
<!DOCTYPE html>
<html lang="fr">
<head>
<meta charset="utf-8">
<title>Maquis Vertex IT – Business Card</title>
<link href="https://fonts.googleapis.com/css2?family=Roboto:wght@400;500&display=swap" rel="stylesheet">
<style>
  :root {
    --backdrop: #c9c9ca;
    --card-grey: #6b6c70;
    --card-white: #ffffff;
    --accent-blue: #2588cc;
    --text-light: #ffffff;
  }
  html, body {
    margin: 0;
    padding: 0;
    width: 1200px;
    height: 930px;
    overflow: hidden;
    background: var(--backdrop);
    font-family: "Roboto", Arial, sans-serif;
  }
  .stage {
    position: relative;
    width: 1200px;
    height: 930px;
  }
  .card {
    position: absolute;
    width: 540px;
    height: 310px;
    background: var(--card-grey);
    color: var(--text-light);
    box-shadow: 0 6px 18px rgba(0,0,0,0.25);
    overflow: hidden;
  }
  .card--logo { left: 70px; top: 140px; }
  .card--contact { left: 590px; top: 480px; }

  /* Logo side */
  .brand-block {
    position: absolute;
    left: 0; right: 0;
    top: 110px;
    display: flex;
    justify-content: center;
    align-items: center;
    gap: 12px;
  }
  .brand-mark {
    width: 14px; height: 14px;
    background: var(--text-light);
  }
  .brand-name {
    font-weight: 500;
    font-size: 34px;
    letter-spacing: 1px;
    text-transform: uppercase;
    color: var(--text-light);
  }
  .legal-line {
    position: absolute;
    left: 0; right: 0;
    bottom: 34px;
    text-align: center;
    font-size: 12px;
    letter-spacing: 0.3px;
  }

  /* Contact side */
  .contact-brand {
    position: absolute;
    left: 34px; top: 56px;
    font-weight: 500;
    font-size: 26px;
    text-transform: uppercase;
    letter-spacing: 0.5px;
  }
  .person {
    position: absolute;
    left: 34px; top: 130px;
  }
  .person-name {
    margin: 0;
    font-weight: 400;
    font-size: 21px;
    letter-spacing: 1px;
    text-transform: uppercase;
  }
  .person-role {
    margin: 2px 0 0;
    font-size: 12px;
  }
  .address {
    position: absolute;
    left: 34px; top: 196px;
    font-size: 13px;
    line-height: 1.35;
    font-style: normal;
  }
  .contact-list {
    position: absolute;
    left: 34px; top: 240px;
    margin: 0; padding: 0;
    list-style: none;
    font-size: 13px;
    line-height: 1.45;
  }
  .contact-list li {
    display: flex;
    align-items: center;
    gap: 8px;
  }
  .contact-icon {
    width: 10px; height: 10px;
    flex: none;
  }
  .graphic-panel {
    position: absolute;
    right: 0; top: 0;
    width: 230px;
    height: 310px;
    background: linear-gradient(160deg, var(--card-white) 0%, #dfe9f2 35%, var(--accent-blue) 60%, var(--card-grey) 100%);
  }
</style>
</head>
<body>
<main class="stage">
  <section class="card card--logo" aria-label="Card front with company name">
    <div class="brand-block">
      <span class="brand-mark" aria-hidden="true"></span>
      <span class="brand-name">Maquis Vertex IT</span>
    </div>
    <p class="legal-line">Siret 71384096200018 APE 6203Y</p>
  </section>

  <section class="card card--contact" aria-label="Card back with contact details">
    <div class="contact-brand">Maquis Vertex IT</div>
    <div class="person">
      <h1 class="person-name">Lucas Moreau</h1>
      <p class="person-role">Director</p>
    </div>
    <address class="address">Centre Commercial<br>Pierre Blanche, 20480 Lorvanu</address>
    <ul class="contact-list">
      <li>
        <svg class="contact-icon" viewBox="0 0 10 10" aria-hidden="true"><path d="M2 1 L4 1 L4.6 3 L3.4 3.8 Q4.4 5.8 6.2 6.6 L7 5.4 L9 6 L9 8 Q8.4 9 7 9 Q1 8 1 2.6 Q1 1.4 2 1 Z" fill="#fff"/></svg>
        <span>0495718243</span>
      </li>
      <li>
        <svg class="contact-icon" viewBox="0 0 10 10" aria-hidden="true"><circle cx="5" cy="5" r="4.3" fill="none" stroke="#fff" stroke-width="1.2"/><path d="M0.8 5 H9.2 M5 0.8 V9.2" stroke="#fff" stroke-width="0.9"/></svg>
        <span>www.maquis-vertex.com</span>
      </li>
      <li>
        <svg class="contact-icon" viewBox="0 0 10 10" aria-hidden="true"><circle cx="5" cy="5" r="4" fill="#fff"/></svg>
        <span>/ateliertech.maquisvertex</span>
      </li>
    </ul>
    <div class="graphic-panel" role="img" aria-label="Geometric arrangement of grey and blue squares on white"></div>
  </section>
</main>
</body>
</html>
```